Mortgage Specialist Wordpress Build

I have a current WordPress site but I would like a whole new site built using the same domain. I've included a site for reference in my outline. The main focus of the website is to educate and capture leads.
I would like my blogs to stay for SEO already earned. Please see work requested attached.
Updates
Project Deadline Extended Reason: I am extending the deadline because I didn't realize this was a design only and I need the website coded as well. I've purchased the add-on. This is my first time using Pixel Bazaar so please bare with me. I have additional Wordpress sites I want to have built too. Thanks, Colin Added Tuesday, April 18, 2017
Target Market(s)
Home Buyers, Home owners looking to refinance or renew their mortgages
Industry/Entity Type
Mortgage
Coding
Coded - Design and coding required
Font styles to use
Look and feel
Each slider illustrates characteristics of the customer's brand and the style your logo design should communicate.

```html
<!DOCTYPE html>
<html lang="en">
<head>
<meta charset="utf-8">
<title>Colin Harwood – Mortgage Specialist</title>
<link rel="stylesheet" href="https://fonts.googleapis.com/css2?family=Lora:wght@700&family=Lato:wght@300;400;700&display=swap">
<style>
:root{
  --navy:#0d3b7e;
  --navy-dark:#0a2e63;
  --yellow:#f7bd1f;
  --grey-bg:#efefef;
  --text:#333;
  --muted:#555;
  --white:#fff;
  --serif:'Lora',Georgia,serif;
  --sans:'Lato',Arial,sans-serif;
}
*{box-sizing:border-box;margin:0;padding:0}
html,body{width:1200px;height:3644px;overflow:hidden}
body{font-family:var(--sans);color:var(--text);background:var(--white);position:relative}
.wrap{width:1030px;margin:0 auto;position:relative}
.btn{display:inline-block;font-family:var(--sans);font-weight:700;text-transform:uppercase;font-size:16px;padding:14px 28px;color:var(--white)}
.btn-yellow{background:var(--yellow);color:#222}
.btn-navy{background:var(--navy)}
.section-title{font-family:var(--serif);font-size:30px;text-align:center;color:#222}
.section-title span{color:var(--navy)}
.title-rule{width:70px;height:3px;background:var(--yellow);margin:18px auto 0}

/* top bar */
.topbar{height:48px;background:var(--navy-dark);color:var(--white);font-size:14px}
.topbar .wrap{display:flex;align-items:center;height:48px;gap:40px}
.topbar .contact{display:flex;align-items:center;gap:10px}
.topbar .socials{margin-left:auto;display:flex;gap:14px}
.topbar .socials i{width:14px;height:14px;border:2px solid var(--white);border-radius:3px;display:block}

/* header */
.site-header{height:98px;background:var(--white)}
.site-header .wrap{display:flex;align-items:center;height:98px}
.brand{font-family:var(--serif);font-size:20px;color:#111;display:flex;align-items:center;gap:10px}
.brand i{width:26px;height:26px;background:#111;display:block}
.main-nav{display:flex;gap:60px;margin-left:170px;font-family:var(--serif);font-size:17px}
.main-nav a{color:#111;text-decoration:none}
.main-nav .active{color:var(--yellow);position:relative}
.main-nav .active:after{content:"";position:absolute;left:8px;right:8px;bottom:-12px;height:3px;background:var(--yellow)}
.badge{margin-left:auto;width:76px;height:76px;border-radius:50%;background:var(--navy)}

/* hero */
.hero{height:494px;position:relative;background:linear-gradient(100deg,#5a5652 0%,#3b3937 45%,#2c2d30 100%);text-align:center;color:var(--white)}
.hero-photo{position:absolute;inset:0}
.hero-inner{position:relative;padding-top:140px}
.play{width:62px;height:62px;margin:0 auto}
.hero h1{font-family:var(--serif);font-size:38px;margin-top:34px}
.hero .actions{margin-top:24px;display:flex;gap:26px;justify-content:center}
.hero .btn{padding:14px 28px;font-size:15px}

/* partners */
.partners{height:248px;background:var(--grey-bg);position:relative}
.partners .section-title{padding-top:44px}
.partner-row{position:absolute;top:128px;left:60px;right:60px;display:flex;justify-content:space-around;align-items:center;height:80px}
.partner{font-family:var(--sans);font-weight:700;font-size:18px;color:#333;display:flex;align-items:center;gap:8px}
.partner i{width:22px;height:22px;background:#555;display:block}
.partner.navy{color:var(--navy)}
.partner.navy i{background:var(--navy)}
.arrow{position:absolute;top:150px;width:20px;height:40px}
.arrow.left{left:30px}.arrow.right{right:30px}

/* help */
.help{height:530px;background:var(--white)}
.help .section-title{padding-top:46px}
.cards{display:flex;justify-content:space-between;margin-top:66px}
.card{width:328px;height:294px;background:var(--white);box-shadow:0 3px 8px rgba(0,0,0,.18);position:relative}
.card .pic{height:218px}
.card h3{font-family:var(--serif);color:var(--navy);font-size:21px;text-align:center;line-height:76px}
.card .icon{position:absolute;left:50%;top:-40px;transform:translateX(-50%);width:92px;height:92px;border-radius:50%;background:var(--yellow);border:5px solid var(--white);display:flex;align-items:center;justify-content:center}

/* question */
.question{height:284px;background:linear-gradient(90deg,#4b4b4b,#5d5d5d 50%,#4a4a4a);color:var(--white);text-align:center;position:relative}
.question h2{font-family:var(--sans);font-weight:300;font-size:56px;padding-top:66px;line-height:1}
.question p{font-size:26px;font-weight:300;margin-top:6px}
.question .btn{margin-top:26px;text-transform:none;padding:12px 46px}

/* faq */
.faq{height:438px}
.faq-head{display:flex;align-items:center;justify-content:space-between;padding-top:48px}
.faq-head h2{font-family:var(--serif);color:#222;font-size:30px}
.faq-head h2 span{color:var(--navy)}
.faq-head .rule{width:70px;height:3px;background:var(--yellow);margin-top:10px}
.faq-head .btn{text-transform:none;padding:12px 30px;font-size:16px}
.faq-cols{display:flex;justify-content:space-between;margin-top:44px}
.faq-item{width:322px}
.faq-item h4{font-size:15px;font-weight:700;line-height:1.4;color:#111}
.faq-item p{font-size:13px;line-height:1.55;color:var(--muted);margin-top:20px}

/* about */
.about{height:668px;background:var(--grey-bg)}
.about .wrap{display:flex;justify-content:space-between;padding-top:60px}
.about-text{width:690px}
.about-text h2{font-family:var(--serif);font-size:28px;color:#222}
.about-text h2 span{color:var(--navy)}
.about-text h3{font-family:var(--serif);font-size:20px;font-weight:700;color:#111;margin:12px 0 16px}
.about-text p{font-size:13px;line-height:1.6;color:#444;margin-bottom:12px}
.about-text a{color:var(--navy);font-weight:700;text-decoration:none}
.about-side{width:298px;text-align:center}
.portrait-frame{position:relative;height:438px}
.portrait-frame:before{content:"";position:absolute;right:-6px;top:-6px;width:280px;height:430px;border-top:6px solid var(--navy);border-right:6px solid var(--navy)}
.portrait{position:absolute;left:0;top:6px;width:292px;height:432px;background:linear-gradient(180deg,#dfe2e6,#b7bcc2 60%,#2a2c30)}
.social{display:flex;justify-content:center;gap:8px;margin-top:16px}
.social i{width:26px;height:26px;background:var(--navy);display:block}
.about-side .btn{margin-top:16px;text-transform:none;font-size:16px;padding:12px 26px}

/* blog */
.blog{height:486px}
.blog .section-title{padding-top:44px}
.posts{display:flex;justify-content:space-between;margin-top:50px}
.post{width:490px;display:flex;gap:22px}
.post .thumb{width:200px;height:230px;position:relative}
.post .thumb:before{content:"";position:absolute;left:-8px;top:-8px;width:100px;height:120px;border-left:4px solid var(--yellow);border-top:4px solid var(--yellow)}
.post .thumb div{width:100%;height:100%}
.post-body{flex:1;padding-top:4px}
.meta{font-size:13px;color:#444;display:flex;gap:24px;padding-bottom:10px;border-bottom:1px solid #ddd}
.post h4{font-family:var(--serif);color:var(--navy);font-size:16px;margin-top:14px}
.post p{font-size:13px;line-height:1.55;color:var(--muted);margin-top:12px}
.more{font-size:13px;font-weight:700;color:#222;margin-top:14px;display:flex;align-items:center;gap:6px}
.blog .center{text-align:center;margin-top:40px}
.blog .center .btn{text-transform:none;padding:12px 34px}

/* subscribe */
.subscribe{height:308px;background:var(--navy);color:var(--white)}
.subscribe .wrap{padding-top:44px;display:flex}
.sub-left{width:700px}
.sub-left h2{font-family:var(--serif);font-size:22px}
.sub-left p{font-size:15px;line-height:1.6;margin-top:24px;width:620px}
.sub-form{display:flex;gap:14px;margin-top:30px}
.sub-form span{width:210px;height:42px;border:1px solid rgba(255,255,255,.7);font-size:14px;padding:12px 10px}
.sub-form .btn{text-transform:none;padding:12px 30px}
.sub-brand{margin-left:auto;display:flex;align-items:center;gap:34px;padding-top:40px}
.sub-brand .brand{color:var(--white)}
.sub-brand .brand i{background:var(--white)}
.sub-brand .badge{width:150px;height:150px;background:var(--white)}

/* footer */
.site-footer{height:42px;background:var(--yellow);font-size:13px;color:#222}
.site-footer .wrap{display:flex;align-items:center;height:42px}
.site-footer .socials{margin-left:auto;display:flex;gap:8px}
.site-footer .socials i{width:22px;height:22px;border:1px solid #222;display:block}
</style>
</head>
<body>

<div class="topbar">
  <div class="wrap">
    <div class="contact">
      <svg width="14" height="14" viewBox="0 0 24 24"><path fill="#fff" d="M6.6 10.8a15 15 0 006.6 6.6l2.2-2.2a1 1 0 011-.25 11.4 11.4 0 003.6.57 1 1 0 011 1V20a1 1 0 01-1 1A17 17 0 013 4a1 1 0 011-1h3.5a1 1 0 011 1c0 1.25.2 2.45.57 3.57a1 1 0 01-.25 1z"/></svg>
      555.014.2290
    </div>
    <div class="contact">
      <svg width="16" height="12" viewBox="0 0 16 12"><rect x="0.5" y="0.5" width="15" height="11" fill="none" stroke="#fff"/><path d="M1 1l7 6 7-6" fill="none" stroke="#fff"/></svg>
      colin@ratehaven.ca
    </div>
    <div class="socials"><i></i><i></i><i></i><i></i><i></i></div>
  </div>
</div>

<header class="site-header">
  <div class="wrap">
    <div class="brand"><i></i>Northgate Lending</div>
    <nav class="main-nav">
      <a class="active">Home</a><a>About Us</a><a>Blog</a><a>Contact Us</a>
    </nav>
    <div class="badge"></div>
  </div>
</header>

<section class="hero">
  <div class="hero-photo" role="img" aria-label="Blurred photo of an office meeting with people at desks"></div>
  <div class="hero-inner">
    <svg class="play" viewBox="0 0 62 62"><circle cx="31" cy="31" r="29" fill="none" stroke="#fff" stroke-width="3"/><path d="M25 19l18 12-18 12z" fill="#fff"/></svg>
    <h1>We Are Mortgage Specialist</h1>
    <div class="actions">
      <span class="btn btn-yellow">Get Hooked Up</span>
      <span class="btn btn-navy">I'm a Client</span>
    </div>
  </div>
</section>

<section class="partners">
  <h2 class="section-title">Some of <span>My Lending Partners</span></h2>
  <svg class="arrow left" viewBox="0 0 20 40"><path d="M18 2L2 20l16 18" fill="none" stroke="#bbb" stroke-width="2"/></svg>
  <div class="partner-row">
    <div class="partner"><i></i>Harbour Bank</div>
    <div class="partner"><i></i>Pine Trust</div>
    <div class="partner"><i></i>Cobalt Credit</div>
    <div class="partner navy"><i></i>Shoreline Financial</div>
    <div class="partner"><i></i>Keystone Mortgages</div>
    <div class="partner"><i></i>Cedar Credit Union</div>
  </div>
  <svg class="arrow right" viewBox="0 0 20 40"><path d="M2 2l16 18L2 38" fill="none" stroke="#bbb" stroke-width="2"/></svg>
</section>

<section class="help">
  <h2 class="section-title">I Need <span>Help With</span></h2>
  <div class="title-rule"></div>
  <div class="wrap cards">
    <div class="card">
      <div class="pic" role="img" aria-label="Hand holding a small model house" style="background:linear-gradient(160deg,#f3f1ee,#e6c9a6)"></div>
      <div class="icon"><svg width="36" height="36" viewBox="0 0 24 24"><path fill="#fff" d="M12 3l10 9h-3v9h-5v-6h-4v6H5v-9H2z"/></svg></div>
      <h3>Purchase</h3>
    </div>
    <div class="card">
      <div class="pic" role="img" aria-label="Model house sitting on banknotes" style="background:linear-gradient(160deg,#c9ccd0,#7d8a8f)"></div>
      <div class="icon"><svg width="36" height="36" viewBox="0 0 24 24"><rect x="6" y="3" width="3" height="18" rx="1.5" fill="#fff"/><rect x="15" y="3" width="3" height="18" rx="1.5" fill="#fff"/></svg></div>
      <h3>Refinance</h3>
    </div>
    <div class="card">
      <div class="pic" role="img" aria-label="Couple meeting with an adviser at a desk" style="background:linear-gradient(160deg,#e8e4de,#9a8d7f)"></div>
      <div class="icon"><svg width="36" height="36" viewBox="0 0 24 24"><rect x="3" y="6" width="18" height="13" rx="2" fill="#fff"/><rect x="14" y="10" width="7" height="5" fill="#f7bd1f"/></svg></div>
      <h3>Renew</h3>
    </div>
  </div>
</section>

<section class="question" role="img" aria-label="Faded photo background behind a call to ask a question">
  <h2>Have a Question</h2>
  <p>about your mortgage or real estate?</p>
  <span class="btn btn-navy">Ask</span>
</section>

<section class="faq">
  <div class="wrap">
    <div class="faq-head">
      <div><h2>FAQ<span>'s</span></h2><div class="rule"></div></div>
      <span class="btn btn-yellow">View All</span>
    </div>
    <div class="faq-cols">
      <div class="faq-item">
        <h4>Lorem ipsum dolor sit amet, ctetuer adipiscing elit, sed diam nonummy nibh euismod?</h4>
        <p>Lorem ipsum dolor sit amet, consectetuer adipiscing elit, sed diam nonummy nibh euismod tincidunt ut laoreet dolore magna aliquam erat volutpat. Ut wisi enim ad minim veniam, quis nostrud exerci tation ullamcorper suscipit lobortis nisl ut aliquip ex ea commodo consequat.</p>
      </div>
      <div class="faq-item">
        <h4>Lorem ipsum dolor sit amet, ctetuer adipiscing elit, sed diam nonummy nibh euismod?</h4>
        <p>Lorem ipsum dolor sit amet, consectetuer adipiscing elit, sed diam nonummy nibh euismod tincidunt ut laoreet dolore magna aliquam erat volutpat. Ut wisi enim ad minim veniam, quis nostrud exerci tation ullamcorper suscipit lobortis nisl ut aliquip ex ea commodo consequat.</p>
      </div>
      <div class="faq-item">
        <h4>Lorem ipsum dolor sit amet, ctetuer adipiscing elit, sed diam nonummy nibh euismod?</h4>
        <p>Lorem ipsum dolor sit amet, consectetuer adipiscing elit, sed diam nonummy nibh euismod tincidunt ut laoreet dolore magna aliquam erat volutpat. Ut wisi enim ad minim veniam, quis nostrud exerci tation ullamcorper suscipit lobortis nisl ut aliquip ex ea commodo consequat.</p>
      </div>
    </div>
  </div>
</section>

<section class="about">
  <div class="wrap">
    <div class="about-text">
      <h2>Colin Harwood <span>– Mortgage Specialist</span></h2>
      <h3>North Vancouver Mortgage Broker</h3>
      <p>Purchasing a home, refinancing a mortgage and renewing a mortgage have one thing in common: they can represent an exciting time in an individual's life but they can also be complex.</p>
      <p>I am dedicated to giving back to the region by helping people save thousands of dollars in interest and prepayment expenses and find solutions that are fitted to your specific situation.</p>
      <p>In addition to getting you a fantastic rate, I ensure that I take enough time for each and every one of my clients to go over every detail in order to see that their mortgage repayment schedule is on track with their financial objectives. It is my mission to help people in this wonderful area get the best North Vancouver mortgage package possible while providing tremendous care and service.</p>
      <p>I offer three main mortgage services to my clients: home purchase, refinance and renewal. Whether it's buying that first home that you've always imagined getting, starting a new business or looking for a more affordable mortgage, I can assure you that I can help solve all of your mortgage goals. The entire mortgage process has the ability to be confusing to those who aren't always directly involved in it and that's why I make my clients' experience as smooth as I can.</p>
      <p>I encourage you to take the time to explore my website and learn as much as you can about me and North Vancouver before we begin the journey. I am always available to answer any questions or concerns you may have, so feel free to reach out to me at any point!</p>
      <p>I am a mortgage broker in North Vancouver who specializes in residential mortgages and am ready to help you with all of your mortgage needs!</p>
      <p>Your <a>North Vancouver Mortgage Broker</a>. I'd love to connect, you can reach me at <a>555.014.2290</a></p>
    </div>
    <div class="about-side">
      <div class="portrait-frame">
        <div class="portrait" role="img" aria-label="Portrait photo of the mortgage specialist"></div>
      </div>
      <div class="social"><i></i><i></i><i></i><i></i><i></i></div>
      <span class="btn btn-yellow">Download My Mortgage App</span>
    </div>
  </div>
</section>

<section class="blog">
  <h2 class="section-title"><span>Latest Blog</span></h2>
  <div class="title-rule"></div>
  <div class="wrap">
    <div class="posts">
      <article class="post">
        <div class="thumb"><div role="img" aria-label="Hands cupped beneath a drawn house outline" style="background:linear-gradient(160deg,#5d88b0,#c9a27a)"></div></div>
        <div class="post-body">
          <div class="meta"><span>14 Apr</span><span>Admin</span></div>
          <h4>Lorem ipsum dolor laort l amet...</h4>
          <p>Lorem ipsum dolor sit aconsectetuer adip iscing elit, sed diam nonummy nibh euismod tincidunt ut laoreet dolore magna aliquam erat volutpat. Ut wisi enim adedianonummy nibh euismod tinlig min nostrud.</p>
          <div class="more">Read More <svg width="14" height="14" viewBox="0 0 14 14"><circle cx="7" cy="7" r="6" fill="none" stroke="#222"/><path d="M5 4l3 3-3 3" fill="none" stroke="#222"/></svg></div>
        </div>
      </article>
      <article class="post">
        <div class="thumb"><div role="img" aria-label="Model house on a white background" style="background:linear-gradient(160deg,#f2f2f2,#b59a80)"></div></div>
        <div class="post-body">
          <div class="meta"><span>14 Apr</span><span>Admin</span></div>
          <h4>Lorem ipsum dolor laoet l amet...</h4>
          <p>Lorem ipsum dolor sit aconsectetuer adip iscing elit, sed diam nonummy nibh euismod tincidunt ut laoreet dolore magna aliquam erat volutpat. Ut wisi enim adedianonummy nibh euismod tinlig min nostrud.</p>
          <div class="more">Read More <svg width="14" height="14" viewBox="0 0 14 14"><circle cx="7" cy="7" r="6" fill="none" stroke="#222"/><path d="M5 4l3 3-3 3" fill="none" stroke="#222"/></svg></div>
        </div>
      </article>
    </div>
    <div class="center"><span class="btn btn-yellow">View All Blog</span></div>
  </div>
</section>

<section class="subscribe">
  <div class="wrap">
    <div class="sub-left">
      <h2>Subscribe To My VIP Club</h2>
      <p>Add your email below to receive my monthly mortgage update AND to join our VIP Club. This is your chance to win a lot of free cool stuff. I promise never to spam you, and I will always keep your email safe!</p>
      <div class="sub-form">
        <span>Name</span><span>Email</span><span class="btn btn-yellow">Subscribe</span>
      </div>
    </div>
    <div class="sub-brand">
      <div class="brand"><i></i>Northgate Lending</div>
      <div class="badge"></div>
    </div>
  </div>
</section>

<footer class="site-footer">
  <div class="wrap">
    <span>© 2017 Colin Harwood - Rate Haven All Rights Reserved. Privacy &amp; Content Notice</span>
    <div class="socials"><i></i><i></i><i></i><i></i><i></i><i></i></div>
  </div>
</footer>

</body>
</html>
```